Beautiful design for wordpress

I need a beautiful, colourful and feminine website. My business is called 'The Moonlit Brook', and I sell crystals, books, CD's, pendulums and other metaphysical items. I also provide Reiki (energy healing).
I want this design to be eye catching and inspire happiness and joy in those who see it. And I would love to see the use of the logo and its colours :)
Please add these on the web design: Home, About, Online store, Blog

• Colourful and playful, must use the logo somewhere, have the words on a menu saying 'Home, Blog, Online store and about' (or similar to those)And the design must stand out!
• grey, brown and other boring colours.

```html
<!DOCTYPE html>
<html lang="en">
<head>
<meta charset="utf-8">
<title>The Moonlit Brook – Crystals &amp; Gifts</title>
<link rel="stylesheet" href="https://fonts.googleapis.com/css2?family=Yesteryear&family=Josefin+Slab:wght@700&family=Oswald:wght@600&display=swap">
<style>
  :root {
    --pink: #ff55dd;
    --orange: #ff9955;
    --brown: #c87137;
    --green: #bcd35f;
    --stone: #7a7a74;
    --paper: #ffffff;
  }
  * { margin: 0; padding: 0; box-sizing: border-box; }
  html, body {
    width: 1200px;
    height: 873px;
    overflow: hidden;
    background: var(--paper);
  }
  .page {
    position: relative;
    width: 1200px;
    height: 873px;
  }
  .main-nav {
    position: absolute;
    top: 30px;
    left: 0;
    width: 1200px;
  }
  .nav-item {
    position: absolute;
    top: 0;
    width: 240px;
    margin-left: -120px;
    text-align: center;
    text-decoration: none;
    display: block;
  }
  .nav-item--home  { left: 193px;  color: var(--pink); }
  .nav-item--about { left: 469px;  color: var(--orange); }
  .nav-item--store { left: 745px;  color: var(--brown); }
  .nav-item--blog  { left: 1021px; color: var(--green); }
  .nav-label {
    display: block;
    height: 90px;
    font-family: "Yesteryear", cursive;
    font-size: 74px;
    line-height: 96px;
    white-space: nowrap;
  }
  .nav-icon {
    display: block;
    width: 145px;
    height: 145px;
    margin: 0 auto;
    border-radius: 50%;
    background: currentColor;
  }
  .nav-icon svg { display: block; width: 145px; height: 145px; }
  .brand {
    position: absolute;
    top: 462px;
    left: 0;
    width: 1200px;
    text-align: center;
    color: var(--stone);
  }
  .brand-name {
    font-family: "Josefin Slab", serif;
    font-weight: 700;
    font-size: 64px;
    line-height: 1;
  }
  .brand-tagline {
    margin-top: 100px;
    font-family: "Oswald", sans-serif;
    font-weight: 600;
    font-size: 15px;
    letter-spacing: 3px;
  }
</style>
</head>
<body>
<div class="page">
  <nav class="main-nav">
    <a class="nav-item nav-item--home" href="#home">
      <span class="nav-label">Home</span>
      <span class="nav-icon">
        <svg viewBox="0 0 145 145" aria-hidden="true">
          <path d="M72 40 L108 72 H98 V104 H80 V84 H64 V104 H46 V72 H36 Z" fill="#fff"/>
        </svg>
      </span>
    </a>
    <a class="nav-item nav-item--about" href="#about">
      <span class="nav-label">About</span>
      <span class="nav-icon">
        <svg viewBox="0 0 145 145" aria-hidden="true">
          <path d="M56 60 A16 16 0 1 1 80 74 Q72 80 72 90" fill="none" stroke="#fff" stroke-width="10" stroke-linecap="round"/>
          <circle cx="72" cy="106" r="6" fill="#fff"/>
        </svg>
      </span>
    </a>
    <a class="nav-item nav-item--store" href="#store">
      <span class="nav-label">Store</span>
      <span class="nav-icon">
        <svg viewBox="0 0 145 145" aria-hidden="true">
          <path d="M58 60 V54 A14 14 0 0 1 86 54 V60" fill="none" stroke="#fff" stroke-width="7"/>
          <path d="M44 60 H100 L96 106 H48 Z" fill="#fff"/>
        </svg>
      </span>
    </a>
    <a class="nav-item nav-item--blog" href="#blog">
      <span class="nav-label">Blog</span>
      <span class="nav-icon">
        <svg viewBox="0 0 145 145" aria-hidden="true">
          <rect x="38" y="44" width="70" height="46" rx="10" fill="#fff"/>
          <path d="M52 88 L50 106 L68 88 Z" fill="#fff"/>
        </svg>
      </span>
    </a>
  </nav>

  <header class="brand">
    <h1 class="brand-name">The Moonlit<br>Brook</h1>
    <p class="brand-tagline">CRYSTALS &amp; GIFTS</p>
  </header>
</div>
</body>
</html>
```